Upmark Velo

We are a new start up company selling (online) innovative cycling products.
Being a new player in the market a modern eye catching logo would be good.
Initially selling safety tail lights with blinkers & modern designed cycling gloves and eventually extending our range into cycling clothing. Many of our products will have a safety theme.

Please see logo attached.
Updates

Project Deadline Extended
Reason: I have extended deadline because i have just received the Logo to be used.

Target Market(s)

We will be target marketing to the young 20-30year old trendy commuter cyclists to the 40 - 60 year old weekend road riders with there immaculate color coordinated road bikes & clothing.

Industry/Entity Type

Safety

Requirements
Must have
• Name: Liam Beck
Line for Mobile No. 0468 923 051
Line for email Address: liam@upmarkvelo.com.au
3 Lines for Postal Address: PO Box 3826
Harlow Vale Crossing
NSW 2157
Website: www.upmarkvelo.com.au

```html
<!DOCTYPE html>
<html lang="en">
<head>
<meta charset="utf-8">
<title>Upmark Velo – Business Card</title>
<link rel="stylesheet" href="https://fonts.googleapis.com/css2?family=Open+Sans:wght@400;700&family=Roboto+Condensed:wght@400&display=swap">
<style>
  :root {
    --stage: #0c0c0c;
    --card: #ffffff;
    --orange: #ee7623;
    --charcoal: #1e1e1e;
    --ink: #1f1f1f;
    --white: #ffffff;
  }
  html, body {
    margin: 0;
    padding: 0;
    width: 1200px;
    height: 900px;
    overflow: hidden;
    background: var(--stage);
  }
  .canvas {
    position: relative;
    width: 1200px;
    height: 900px;
    background: var(--stage);
  }
  .card {
    position: absolute;
    left: 122px;
    top: 165px;
    width: 955px;
    height: 569px;
    background: var(--card);
    overflow: hidden;
  }
  .name-banner {
    position: absolute;
    left: 0;
    top: 95px;
    width: 422px;
    height: 110px;
  }
  .name-banner svg { position: absolute; inset: 0; }
  .holder-name {
    position: absolute;
    left: 53px;
    top: 17px;
    margin: 0;
    font-family: "Open Sans", sans-serif;
    font-weight: 400;
    font-size: 38px;
    line-height: 1;
    color: var(--white);
    letter-spacing: 0.2px;
  }
  .holder-role {
    position: absolute;
    left: 58px;
    top: 66px;
    margin: 0;
    font-family: "Open Sans", sans-serif;
    font-size: 19px;
    line-height: 1;
    color: var(--white);
  }
  .contact-list {
    position: absolute;
    left: 53px;
    top: 273px;
    margin: 0;
    padding: 0;
    list-style: none;
  }
  .contact-item {
    display: flex;
    align-items: center;
    height: 32px;
    margin-bottom: 12px;
    font-family: "Roboto Condensed", sans-serif;
    font-size: 20px;
    color: var(--ink);
  }
  .contact-icon {
    width: 32px;
    height: 32px;
    margin-right: 13px;
    flex: none;
  }
  .brand-name {
    position: absolute;
    left: 498px;
    top: 386px;
    margin: 0;
    font-family: "Open Sans", sans-serif;
    font-weight: 700;
    font-size: 52px;
    line-height: 1;
    color: var(--ink);
    letter-spacing: -0.5px;
  }
  .band-charcoal {
    position: absolute;
    left: 0;
    top: 498px;
    width: 100%;
    height: 32px;
    background: var(--charcoal);
  }
  .band-orange {
    position: absolute;
    left: 0;
    top: 530px;
    width: 100%;
    height: 39px;
    background: var(--orange);
  }
</style>
</head>
<body>
<div class="canvas">
  <section class="card">
    <div class="name-banner">
      <svg width="422" height="110" viewBox="0 0 422 110" aria-hidden="true">
        <polygon points="0,0 422,0 361,110 0,110" fill="var(--orange)"/>
      </svg>
      <h1 class="holder-name">LIAM BECK</h1>
      <p class="holder-role">Manager</p>
    </div>

    <ul class="contact-list">
      <li class="contact-item">
        <svg class="contact-icon" viewBox="0 0 32 32" aria-hidden="true">
          <circle cx="16" cy="16" r="16" fill="var(--orange)"/>
          <path d="M16 7a6 6 0 0 0-6 6c0 4.5 6 12 6 12s6-7.5 6-12a6 6 0 0 0-6-6z" fill="var(--white)"/>
          <circle cx="16" cy="13" r="2.3" fill="var(--orange)"/>
        </svg>
        PO Box 3826, Harlow Vale Crossing , NSW 2157
      </li>
      <li class="contact-item">
        <svg class="contact-icon" viewBox="0 0 32 32" aria-hidden="true">
          <circle cx="16" cy="16" r="16" fill="var(--orange)"/>
          <rect x="11" y="7" width="10" height="18" rx="1.5" fill="none" stroke="var(--white)" stroke-width="1.8"/>
          <rect x="13" y="10" width="6" height="5" fill="var(--white)"/>
          <g fill="var(--white)">
            <rect x="13" y="17" width="1.6" height="1.6"/><rect x="15.2" y="17" width="1.6" height="1.6"/><rect x="17.4" y="17" width="1.6" height="1.6"/>
            <rect x="13" y="19.6" width="1.6" height="1.6"/><rect x="15.2" y="19.6" width="1.6" height="1.6"/><rect x="17.4" y="19.6" width="1.6" height="1.6"/>
          </g>
        </svg>
        0468 923 051
      </li>
      <li class="contact-item">
        <svg class="contact-icon" viewBox="0 0 32 32" aria-hidden="true">
          <circle cx="16" cy="16" r="16" fill="var(--orange)"/>
          <rect x="7" y="10" width="18" height="12" fill="none" stroke="var(--white)" stroke-width="1.8"/>
          <path d="M7 10l9 7 9-7M7 22l7-6M25 22l-7-6" fill="none" stroke="var(--white)" stroke-width="1.6"/>
        </svg>
        liam@upmarkvelo.com.au
      </li>
      <li class="contact-item">
        <svg class="contact-icon" viewBox="0 0 32 32" aria-hidden="true">
          <circle cx="16" cy="16" r="16" fill="var(--orange)"/>
          <g fill="none" stroke="var(--white)" stroke-width="2" stroke-linecap="round">
            <path d="M14.5 17.5l-2.5 2.5a2.8 2.8 0 0 1-4-4l3-3a2.8 2.8 0 0 1 4 0"/>
            <path d="M17.5 14.5l2.5-2.5a2.8 2.8 0 0 1 4 4l-3 3a2.8 2.8 0 0 1-4 0"/>
            <path d="M13.5 18.5l5-5"/>
          </g>
        </svg>
        www.upmarkvelo.com.au
      </li>
    </ul>

    <p class="brand-name">Upmark Velo</p>

    <div class="band-charcoal"></div>
    <div class="band-orange"></div>
  </section>
</div>
</body>
</html>
```